Kestrel Lane flyer

Need a A6 size horizontal layout flyer. See attached example for ideas as well as some images I have which you can use. we are a hire car company that provides vehicles to clients who have recently been involved in car accidents and who's cars are currently getting fixed and so they lose the use of their own vehicle. see our website to keep flyer in line with website and for any further information kestrellane.com.au

Target Market(s)

people involved in not at fault car accidents

Industry/Entity Type

It Company

Requirements
Must have
• *ask people to let us know where they got our flyer from when they call us
• *call to action for people to call our phone number 1800 417 582
Should not have
• any mentioning that the vehicle is free

```html
<!DOCTYPE html>
<html lang="en">
<head>
<meta charset="utf-8">
<title>Kestrel Lane Flyer</title>
<link href="https://fonts.googleapis.com/css2?family=Questrial&family=Fjalla+One&display=swap" rel="stylesheet">
<style>
  :root {
    --page: #e4e4e4;
    --blue: #3d8fe6;
    --blue-light: #5aa7f0;
    --blue-dark: #1f6fd6;
    --yellow: #fbb516;
    --yellow-text: #f6b51a;
    --charcoal: #3a3a3a;
    --grey-text: #6f6f6f;
    --white: #ffffff;
    --frame: #d8d8d8;
  }
  * { margin: 0; padding: 0; box-sizing: border-box; }
  html, body { width: 802px; height: 1200px; overflow: hidden; }
  body { background: var(--page); font-family: "Questrial", sans-serif; position: relative; }

  .flyer {
    position: absolute; left: 0; top: 315px;
    width: 802px; height: 570px; overflow: hidden;
    background: var(--white);
    box-shadow: 0 6px 18px rgba(0,0,0,.25);
  }
  .flyer-art { position: absolute; inset: 0; }

  .brand-name {
    position: absolute; left: 245px; width: 320px; top: 140px;
    text-align: center; color: var(--white); font-size: 31px; letter-spacing: .3px;
  }

  .tagline {
    position: absolute; top: 246px; left: 0; width: 802px; text-align: center;
    font-size: 18px; line-height: 24px; color: var(--grey-text);
  }
  .tagline .accent { color: var(--blue-dark); }

  .step-label {
    position: absolute; top: 366px; text-align: center;
    color: var(--white); font-size: 13px; line-height: 17px; letter-spacing: .2px;
  }
  .step-apply { left: 25px; width: 225px; top: 362px; }
  .step-apply .flyer-source { display: block; font-size: 10.5px; line-height: 14px; margin-top: 3px; letter-spacing: .3px; }
  .step-details { left: 300px; width: 215px; top: 368px; }
  .step-replace { left: 570px; width: 220px; }

  .about {
    position: absolute; left: 45px; top: 438px; width: 425px; color: var(--white);
  }
  .about-title { font-size: 19px; font-weight: normal; letter-spacing: .3px; }
  .about-rule { width: 62px; height: 3px; background: var(--yellow); margin: 3px 0 10px; }
  .about-body { font-size: 12.4px; line-height: 16.2px; text-align: justify; }

  .offer {
    position: absolute; left: 521px; top: 452px; width: 255px; height: 87px;
    border: 2px solid #bfbfbf; text-align: center; color: var(--yellow-text);
    font-family: "Fjalla One", sans-serif;
  }
  .offer-head { font-size: 31px; line-height: 38px; margin-top: 6px; letter-spacing: 1px; }
  .offer-sub { font-size: 19px; line-height: 24px; }

  .web {
    position: absolute; left: 521px; top: 542px; width: 255px; text-align: center;
    color: var(--white); font-size: 17px; letter-spacing: .3px;
  }
  .web .accent { color: var(--yellow-text); }
</style>
</head>
<body>
  <article class="flyer">
    <svg class="flyer-art" width="802" height="570" viewBox="0 0 802 570">
      <defs>
        <linearGradient id="carPhoto" x1="0" y1="0" x2="1" y2="1">
          <stop offset="0" stop-color="#4a4a48"/>
          <stop offset=".5" stop-color="#d9dadb"/>
          <stop offset="1" stop-color="#6d6d6b"/>
        </linearGradient>
        <linearGradient id="driversPhoto" x1="0" y1="0" x2="1" y2="1">
          <stop offset="0" stop-color="#a7b2bd"/>
          <stop offset=".5" stop-color="#e3d6cc"/>
          <stop offset="1" stop-color="#5d6570"/>
        </linearGradient>
        <radialGradient id="heroBlue" cx=".5" cy=".4" r=".7">
          <stop offset="0" stop-color="#4e9ff0"/>
          <stop offset="1" stop-color="#2f7fdb"/>
        </radialGradient>
        <linearGradient id="aboutBand" x1="0" y1="0" x2="0" y2="1">
          <stop offset="0" stop-color="#444"/>
          <stop offset="1" stop-color="#262626"/>
        </linearGradient>
      </defs>

      <rect class="hero-blue" x="0" y="0" width="802" height="240" fill="url(#heroBlue)"/>
      <polygon class="photo-car" role="img" aria-label="Photo of a white car front with headlight, on a tree-lined road"
               points="0,0 245,0 282,120 245,240 0,240" fill="url(#carPhoto)"/>
      <polyline points="245,0 282,120 245,240" fill="none" stroke="var(--frame)" stroke-width="5"/>
      <polygon class="photo-drivers" role="img" aria-label="Photo of a smiling couple driving a car"
               points="562,0 802,0 802,240 562,240 522,120" fill="url(#driversPhoto)"/>
      <polyline points="562,0 522,120 562,240" fill="none" stroke="var(--frame)" stroke-width="5"/>

      <polygon class="step-band-yellow" points="0,327 270,327 295,378 270,428 0,428" fill="var(--yellow)"/>
      <polygon class="step-band-mid" points="270,327 530,327 555,378 530,428 270,428 295,378" fill="var(--blue-light)"/>
      <polygon class="step-band-deep" points="530,327 802,327 802,428 530,428 555,378" fill="var(--blue-dark)"/>
      <polyline points="270,327 295,378 270,428" fill="none" stroke="#fff" stroke-width="2"/>
      <polyline points="530,327 555,378 530,428" fill="none" stroke="#fff" stroke-width="2"/>

      <g class="icon-form" transform="translate(138,327)">
        <circle r="27" fill="var(--yellow)" stroke="#fff" stroke-width="3"/>
        <rect x="-10" y="-13" width="18" height="24" rx="2" fill="none" stroke="#fff" stroke-width="2.4"/>
        <line x1="-6" y1="-5" x2="4" y2="-5" stroke="#fff" stroke-width="2"/>
        <line x1="-6" y1="0" x2="4" y2="0" stroke="#fff" stroke-width="2"/>
        <line x1="-6" y1="5" x2="0" y2="5" stroke="#fff" stroke-width="2"/>
        <circle cx="8" cy="9" r="6" fill="#fff"/>
        <polyline points="5,9 7.5,11.5 11,6.5" fill="none" stroke="var(--yellow)" stroke-width="1.8"/>
      </g>
      <g class="icon-phone" transform="translate(405,327)">
        <circle r="27" fill="var(--blue-light)" stroke="#fff" stroke-width="3"/>
        <path d="M-12,-8 q-2,14 16,20 l4,-5 -6,-4 -3,3 q-7,-3 -8,-10 l3,-3 -4,-6 z" fill="#fff"/>
        <ellipse cx="6" cy="-8" rx="8" ry="6" fill="#fff"/>
        <circle cx="3" cy="-8" r="1.2" fill="var(--blue-light)"/>
        <circle cx="6" cy="-8" r="1.2" fill="var(--blue-light)"/>
        <circle cx="9" cy="-8" r="1.2" fill="var(--blue-light)"/>
      </g>
      <g class="icon-car" transform="translate(673,327)">
        <circle r="27" fill="var(--blue-dark)" stroke="#fff" stroke-width="3"/>
        <path d="M-15,4 v-5 q0,-3 4,-3 l5,-6 h12 l5,6 q5,0 5,4 v4 z" fill="#fff"/>
        <rect x="-5" y="-8" width="5" height="4" fill="var(--blue-dark)"/>
        <rect x="2" y="-8" width="5" height="4" fill="var(--blue-dark)"/>
        <circle cx="-8" cy="5" r="3.5" fill="#fff" stroke="var(--blue-dark)" stroke-width="1.5"/>
        <circle cx="8" cy="5" r="3.5" fill="#fff" stroke="var(--blue-dark)" stroke-width="1.5"/>
      </g>

      <rect class="about-band" x="0" y="428" width="802" height="142" fill="url(#aboutBand)"/>
    </svg>

    <div class="brand-name">Kestrel Lane</div>

    <p class="tagline">ARRANGING AN ACCIDENT REPLACEMENT VEHICLE<br>
      <span class="accent">FOR YOURSELF</span> IS EASY AS <span class="accent">1,2,3</span></p>

    <p class="step-label step-apply">APPLY ONLINE OR CALL<br>1800 417 582
      <span class="flyer-source">TELL US WHERE YOU GOT THIS FLYER</span></p>
    <p class="step-label step-details">PROVIDE<br>ACCIDENT DETAILS</p>
    <p class="step-label step-replace">YOU GET A REPLACEMENT<br>VEHICLEWE TAKE<br>CARE OF THE REST</p>

    <section class="about">
      <h2 class="about-title">ABOUT US</h2>
      <div class="about-rule"></div>
      <p class="about-body">When you’re in an accident, and it’s not your fault, it’s hard to overcome the various obstacles that you man now face. For example, because someone else caused an accident, you’re now inconvenienced by not having a car to drive. It hardly seems fair, and that’s why you need to look at a not at fault accident rental car.</p>
    </section>

    <div class="offer">
      <div class="offer-head">FREE DELIVERY</div>
      <div class="offer-sub">LATE MODEL/NEW VEHICLES</div>
    </div>
    <div class="web">www.<span class="accent">kestrellane</span>.com.au</div>
  </article>
</body>
</html>
```